Design cd cover for the vocal group: Ember, cd title Harbor Light. Cd cover is for EP release to be followed by full album. Songs are: Sizwe Langa Khona(Lift high the lamp); Cold River Road; Ngolwazi(Guide me through the night); When Rain Falls. There is no track entitled harbor light; the concept of the sound of gospel music as embodied in the music tracks - contemporary and traditional - is the basis of the album title.
NB: Project can close Tuesday 12 November to account for the 5 days as I do not count Saturday as a working day.
Hey guys,
Hello to everyone. I would like to take this opportunity to say thank you for your participation. Your submissions have been great and much appreciated. Forgive me for not being able to provide feedback to all of you. The time has come for me to make selection decisions and I would like to say thank you to all for your participation, you have been great and amazing.

```html
<!DOCTYPE html>
<html lang="en">
<head>
<meta charset="utf-8">
<title>Harbor Light — Ember</title>
<link rel="stylesheet" href="https://fonts.googleapis.com/css2?family=Jost:wght@300;400&display=swap">
<style>
  :root {
    --sky-teal: #3aa9b6;
    --sky-blue: #2f7fb2;
    --sky-cyan: #78d3dc;
    --cloud-cream: #f6ece2;
    --cloud-blush: #e2b7c4;
    --cloud-rose: #b86a98;
    --title-cyan: #8cf0f0;
    --title-white: #ffffff;
    --text-white: #f7fbfc;
  }
  html, body {
    margin: 0;
    padding: 0;
    width: 1200px;
    height: 1200px;
    overflow: hidden;
    background: #ffffff;
  }
  .cover {
    position: relative;
    width: 1200px;
    height: 1200px;
    overflow: hidden;
    font-family: "Jost", "Futura", sans-serif;
  }
  .cover__sky {
    position: absolute;
    inset: 0;
    background:
      radial-gradient(ellipse 55% 35% at 85% 55%, rgba(255,248,240,0.75), rgba(255,248,240,0) 70%),
      radial-gradient(ellipse 70% 30% at 35% 92%, rgba(250,240,232,0.95), rgba(250,240,232,0) 75%),
      radial-gradient(ellipse 50% 35% at 90% 95%, rgba(184,106,152,0.85), rgba(184,106,152,0) 75%),
      radial-gradient(ellipse 40% 25% at 5% 85%, rgba(226,183,196,0.8), rgba(226,183,196,0) 75%),
      radial-gradient(ellipse 45% 40% at 30% 20%, rgba(150,215,225,0.45), rgba(150,215,225,0) 70%),
      linear-gradient(180deg, var(--sky-teal) 0%, var(--sky-cyan) 22%, var(--sky-blue) 52%, #6a9cc6 68%, var(--cloud-blush) 85%, var(--cloud-cream) 100%);
  }
  .cover__title {
    position: absolute;
    margin: 0;
    font-weight: 300;
    font-size: 172px;
    line-height: 1;
    letter-spacing: 0.2em;
    white-space: nowrap;
    color: var(--title-white);
    background: linear-gradient(90deg, var(--title-cyan) 0%, var(--title-cyan) 58%, var(--title-white) 70%, var(--title-white) 100%);
    background-size: 1200px 100%;
    -webkit-background-clip: text;
    background-clip: text;
    -webkit-text-fill-color: transparent;
  }
  .cover__title-line {
    position: absolute;
    display: block;
  }
  .cover__title-line--first {
    left: 60px;
    top: 340px;
    background-position: -60px 0;
  }
  .cover__title-line--second {
    left: 400px;
    top: 490px;
    background-position: -400px 0;
  }
  .cover__subtitle {
    position: absolute;
    left: 0;
    width: 1060px;
    top: 670px;
    margin: 0;
    text-align: center;
    font-weight: 300;
    font-size: 60px;
    letter-spacing: 0.12em;
    color: var(--text-white);
    white-space: nowrap;
  }
  .cover__artist {
    position: absolute;
    left: 0;
    right: 0;
    top: 1090px;
    margin: 0;
    text-align: center;
    font-weight: 400;
    font-size: 36px;
    letter-spacing: 0.2em;
    color: var(--text-white);
  }
</style>
</head>
<body>
  <main class="cover">
    <div class="cover__sky" role="img" aria-label="Sky photograph with sun rays breaking through blue sky over soft cream and pink clouds"></div>
    <h1 class="cover__title-wrap">
      <span class="cover__title cover__title-line cover__title-line--first">HARBOR</span>
      <span class="cover__title cover__title-line cover__title-line--second">LIGHT</span>
    </h1>
    <p class="cover__subtitle">SIZWE LANGA KHONA</p>
    <p class="cover__artist">EMBER</p>
  </main>
</body>
</html>
```